I need to re design my current Business Proposal , More professional and beautiful

We currently use a power point template to create our business proposal for construction projects ,we use powerpoint to create the template then we export to PDF.

i like it but i think it can be better, i will upload our current powerpoint template, PDF Example, Our Company Brochure (so you can see the level of design we are expecting.

Page 1 - Front Cover ( make sure you incorporate the picture of all the techs) -------REDESIGN
Page 2 - Introduction Page - PLEASE SIMPLE DETAILS
Page 3 - Scope of Work - PLEASE SIMPLE DETAILS
Page 4 - Classification and Exclusion Page- PLEASE SIMPLE DETAILS
Page 5 Pricing - PLEASE SIMPLE DETAILS
Page 6 - Payment Schedule - PLEASE SIMPLE DETAILS
Page 7 References -----REDESIGN
Page 8 Recent Projects-----REDESIGN
Page 9 Certification and lets add the brand logos of Manufacturer we work with ( see brochure) -----REDESIGN

Also here is google drive link with some pictures
https://filevault-share.example/folders/7kzq_RRMxhw93PLu2bWnTe8-Yd4c?usp=sharing

also you can download more pics from our website

nexbuildgroup.com

```html
<!DOCTYPE html>
<html lang="en">
<head>
<meta charset="utf-8">
<title>NexBuild Technologies – Proposal Template</title>
<link href="https://fonts.googleapis.com/css2?family=Open+Sans:ital,wght@0,400;0,600;0,700;0,800;1,400&family=Montserrat:wght@400;700;800&display=swap" rel="stylesheet">
<style>
:root{
  --navy:#0c2346;
  --blue:#00a3df;
  --yellow:#f5c200;
  --red:#e5331c;
  --green:#6ab42d;
  --ink:#2b2b2b;
  --stage:#cbcbcb;
  --photo-a:#3d5a7a;
  --photo-b:#8a9aa8;
}
*{margin:0;padding:0;box-sizing:border-box}
html,body{width:942px;height:1200px;overflow:hidden;background:var(--stage)}
body{position:relative;font-family:"Open Sans",Arial,sans-serif;color:var(--ink)}
.page{position:absolute;width:259px;height:335px;background:#fff;overflow:hidden}
.p-cover{left:71px;top:84px;background:var(--navy)}
.p2{left:341px;top:84px}.p3{left:612px;top:84px}
.p4{left:71px;top:432px}.p5{left:341px;top:432px}.p6{left:612px;top:432px}
.p7{left:71px;top:781px}.p8{left:341px;top:781px}.p9{left:612px;top:781px}

.hdr{position:absolute;left:0;top:0;width:100%;height:35px;background:var(--navy)}
.brand{position:absolute;left:12px;top:10px;display:flex;align-items:center;gap:3px;color:#fff;font-family:"Montserrat",sans-serif;font-size:5.5px;letter-spacing:.6px}
.brand .mark{width:7px;height:7px;background:var(--blue)}
.brand small{display:block;font-size:2.6px;letter-spacing:1px;color:#cfe3f5}
.sub{position:absolute;right:17px;top:27px;color:#d8e4f0;font-size:3.3px}
.band{position:absolute;left:0;top:35px;width:100%;height:21px;background:var(--blue);color:#fff;font-weight:700;font-size:10px;letter-spacing:.4px;padding:6px 0 0 47px;line-height:1}
.band.tall{height:34px;padding-top:7px;line-height:1.05}
.foot{position:absolute;left:0;bottom:0;width:100%;height:15px;background:var(--navy)}
.foot .stripe{display:flex;height:2px}
.foot .stripe i{flex:1}
.foot .stripe i:nth-child(1){background:var(--red)}
.foot .stripe i:nth-child(2){background:var(--yellow)}
.foot .stripe i:nth-child(3){background:var(--green)}
.foot .url{position:absolute;left:15px;top:4px;color:#fff;font-size:3.4px}
.foot .num{position:absolute;right:15px;top:4px;color:var(--blue);font-size:5.5px;font-weight:700}

.bullets{position:absolute;left:49px;top:71px;width:180px;list-style:none;font-size:4.8px;line-height:1.95}
.bullets li{position:relative;padding-left:11px;margin-bottom:7.5px}
.bullets li::before{content:"";position:absolute;left:0;top:2px;width:4.5px;height:4.5px;border:1.2px solid var(--red);border-radius:50%}

/* cover */
.cover-brand{position:absolute;left:0;top:22px;width:100%;text-align:center;color:#fff;font-family:"Montserrat",sans-serif}
.cover-brand .name{display:inline-flex;align-items:center;gap:5px;font-size:8.5px;letter-spacing:1px}
.cover-brand .name i{width:12px;height:12px;background:var(--blue)}
.cover-brand .rule{width:122px;margin:6px auto 0;border-top:.6px solid #9fb6cc;border-bottom:.6px solid #9fb6cc;font-family:"Open Sans",sans-serif;font-size:4.2px;padding:1.5px 0}
.hero{position:absolute;left:0;top:62px;width:100%;height:158px;background:linear-gradient(180deg,#6f8fb3 0%,#4a6784 45%,var(--photo-a) 75%,#22375a 100%)}
.hero .offices{position:absolute;top:2px;width:100%;text-align:center;color:#fff;font-size:3.4px}
.cover-title{position:absolute;left:20px;top:183px;color:#fff;font-family:"Montserrat",sans-serif;font-weight:800;font-size:38px;letter-spacing:.5px;line-height:1}
.cover-panel{position:absolute;left:0;top:220px;width:100%;height:77px;background:var(--blue)}
.cover-for{position:absolute;left:21px;top:0;font-family:"Montserrat",sans-serif;font-weight:700;color:var(--navy);font-size:14px}
.cover-lines{position:absolute;left:21px;top:27px;width:71px}
.cover-lines i{display:block;height:13px;border-bottom:.6px solid var(--navy)}
.cover-table{position:absolute;left:105px;top:6px;width:141px;border-collapse:collapse;font-size:3.6px;color:var(--navy);font-weight:600}
.cover-table td{border:.6px solid #fff;padding:0 2px;height:6.6px}
.cover-table td:first-child{width:63px}
.cover-table td.v{color:var(--navy);font-weight:400}
.notice{position:absolute;left:21px;top:303px;width:215px;color:#fff;font-size:3.1px;line-height:1.4}
.notice b{display:block;font-size:3.4px;margin-bottom:4px}

/* intro */
.letter{position:absolute;left:47px;top:71px;width:168px;font-size:4.8px;line-height:1.6}
.letter p{margin-bottom:7px}
.letter .date{font-style:italic;margin-bottom:25px}

/* pricing */
.price-table{position:absolute;left:36px;top:73px;width:188px;height:221px;border:.8px solid var(--navy);border-radius:5px;overflow:hidden}
.price-table .th,.price-table .tf{position:absolute;left:0;width:100%;height:9px;background:var(--yellow);font-size:4.7px;font-weight:700;color:var(--navy)}
.price-table .th{top:0}.price-table .tf{bottom:0;text-align:center;padding-top:1.5px}
.price-table .th span{position:absolute;top:1.8px}
.price-table .col{position:absolute;top:0;bottom:0;border-left:.8px solid var(--navy)}

/* payment */
.pay-note{position:absolute;left:47px;top:120px;width:170px;font-size:4.8px;line-height:1.45}
.signed{position:absolute;left:47px;top:160px;color:var(--blue);font-weight:700;font-size:10px}
.sig{position:absolute;font-size:4.8px;line-height:1.45}
.sig-line{position:absolute;border-top:.6px solid #555}

/* references */
.ref-table{position:absolute;left:36px;top:77px;width:188px;height:188px;border:.8px solid var(--navy);border-radius:5px;overflow:hidden}
.ref-table .th{height:9px;background:var(--yellow);font-size:4.7px;font-weight:700;color:var(--navy);position:relative}
.ref-table .th span{position:absolute;top:1.8px}
.ref-table .divider{position:absolute;left:19px;top:0;bottom:0;border-left:.8px solid var(--navy)}
.ref{position:absolute;left:23px;font-size:3.9px;line-height:1.45}
.ref b{color:var(--red);font-weight:700}
.ref-no{position:absolute;left:6px;width:7px;height:7px;border:1px solid var(--red);border-radius:50%;font-size:3.6px;font-weight:700;color:var(--red);text-align:center;line-height:5px}
.clients{position:absolute;left:36px;top:273px;width:196px;display:grid;grid-template-columns:repeat(5,1fr);row-gap:7px;font-size:4.4px;color:var(--navy);font-weight:600;text-align:center}

/* projects */
.proj-table{position:absolute;left:36px;top:68px;width:188px;height:242px;border:.8px solid var(--navy);border-radius:5px;overflow:hidden}
.proj-table .th{height:10px;background:var(--yellow);font-size:4.7px;font-weight:700;color:var(--navy);padding:2px 0 0 8px;position:relative}
.proj-table .th::after{content:"";position:absolute;left:66px;top:0;bottom:0;border-left:.8px solid var(--navy)}
.proj-row{position:relative;height:38.6px;border-top:.8px solid var(--navy)}
.proj-row:first-of-type{border-top:none}
.proj-row .pname{position:absolute;left:8px;top:50%;transform:translateY(-50%);width:56px;font-size:4px;font-weight:700;line-height:1.3}
.proj-row .shots{position:absolute;left:66px;top:0;right:0;bottom:0;display:flex;gap:.8px;background:var(--navy)}
.proj-row .shots span{flex:1;background:linear-gradient(160deg,var(--photo-b),#3f4c5c)}
.proj-row:nth-of-type(4) .shots span{background:linear-gradient(160deg,#b9c2cb,#707a86)}
.proj-row:nth-of-type(5) .shots span{background:linear-gradient(160deg,#8b4d8f,#2c3344)}
.proj-row:nth-of-type(6) .shots span{background:linear-gradient(160deg,#8a5a4a,#303846)}

/* certification */
.cert-text{position:absolute;left:47px;top:73px;width:172px;font-size:4.8px;line-height:1.45}
.cert-photo{position:absolute;left:47px;top:140px;width:105px;height:139px;border:.8px solid var(--blue);background:linear-gradient(180deg,#c7ccd0 0%,#7a8189 55%,#3b4047 100%)}
</style>
</head>
<body>

<!-- Cover -->
<section class="page p-cover">
  <div class="cover-brand">
    <div class="name"><i></i>NEXBUILD TECHNOLOGIES</div>
    <div class="rule">A Subsidiary of Guardline Alarm Division</div>
  </div>
  <div class="hero" role="img" aria-label="Team photo of the company's cabling technicians standing in front of the office and vans">
    <div class="offices">Offices Miami - Ft. Lauderdale - Palm Beach</div>
  </div>
  <div class="cover-title">PROPOSAL</div>
  <div class="cover-panel">
    <div class="cover-for">For</div>
    <div class="cover-lines"><i></i><i></i><i></i></div>
    <table class="cover-table">
      <tr><td>NBT CONTRACT NAME:</td><td class="v"></td></tr>
      <tr><td style="height:27px">PROPERTY LOCATION:</td><td class="v"></td></tr>
      <tr><td>PROPOSAL DESCRIPTION:</td><td class="v"></td></tr>
      <tr><td>DATE OF PROPOSAL:</td><td class="v">10/31/2023</td></tr>
      <tr><td>ATTN:</td><td class="v"></td></tr>
      <tr><td>QUOTE#</td><td class="v"></td></tr>
    </table>
  </div>
  <div class="notice">
    <b>NOTICE OF PROPRIETARY INFORMATION</b>
    The contents of this package are considered by NexBuild Technologies Inc to be proprietary. This document is intended for the sole use of the customer and may not be released to any other vendor or contractor without written permission from NexBuild Technologies.
  </div>
</section>

<!-- Introduction -->
<section class="page p2">
  <header class="hdr"><div class="brand"><span class="mark"></span><span>NEXBUILD<small>TECHNOLOGIES</small></span></div><div class="sub">A Subsidiary of Guardline Alarm Division</div></header>
  <h2 class="band">INTRODUCTION</h2>
  <div class="letter">
    <p class="date">October 31, 2023</p>
    <p><b>Dear Mr. Owen Hale,</b></p>
    <p>Thank you for providing us with the opportunity to present this Proposal addressing your Structured cabling needs.</p>
    <p>For over 15 years, NexBuild Technologies has provided excellent low voltage services and solutions for organizations and commercial clients in South Florida. We have successfully completed thousands of structured cabling projects for offices, retail centers, churches, and schools. We stand by our work and guarantee excellent quality and materials. We adhere to safety standards and meet all safety regulations of the state.</p>
    <p>Included in this proposal, you will find a complete solution designed to meet your structured cabling needs. We know time is of the essence, so please don't hesitate to contact me with any further questions.</p>
    <p>Thank again for considering NexBuild Technologies as your partner for your Structured cabling needs.</p>
    <p>We look forward to working with you.</p>
    <p style="margin-top:12px"><b>Sincerely,</b></p>
    <p>Leo Marquez</p>
  </div>
  <footer class="foot"><div class="stripe"><i></i><i></i><i></i></div><span class="url">www.nexbuildgroup.com</span><span class="num">1</span></footer>
</section>

<!-- Scope -->
<section class="page p3">
  <header class="hdr"><div class="brand"><span class="mark"></span><span>NEXBUILD<small>TECHNOLOGIES</small></span></div><div class="sub">A Subsidiary of Guardline Alarm Division</div></header>
  <h2 class="band">SCOPE OF WORK</h2>
  <ul class="bullets" style="top:73px">
    <li>NBT will Label every cable for easy identification</li>
    <li>NBT will test , and label all the cabling and terminations</li>
    <li>NBT will follow State low voltage Code installation procedures, and also follow best practices and guidelines by TCSA (Telecom Cabling Standards Association)</li>
    <li>NBT will dressed the cables and terminate them in clean organized way.</li>
    <li>2 Year Labor Warranty / 15 Manufacturer Warranty</li>
  </ul>
  <footer class="foot"><div class="stripe"><i></i><i></i><i></i></div><span class="url">www.nexbuildgroup.com</span><span class="num">2</span></footer>
</section>

<!-- Clarifications -->
<section class="page p4">
  <header class="hdr"><div class="brand"><span class="mark"></span><span>NEXBUILD<small>TECHNOLOGIES</small></span></div><div class="sub">A Subsidiary of Guardline Alarm Division</div></header>
  <h2 class="band">CLARIFICATIONS AND EXCLUSION</h2>
  <ul class="bullets" style="top:70px;width:175px">
    <li>NBT will install materials that meet / exceeds the highest performance and durability standards. All the materials will carry a UL / ETL Listing.</li>
    <li>All conduit, junction boxes, fittings and Stub ups will be provided by others.</li>
    <li>NBT will follow State low voltage Code installation procedures, and also follow best practices and guidelines by TCSA (Telecom Cabling Standards Association) .</li>
    <li>NBT will dressed the cables and terminate them in clean organized way.</li>
    <li>2 Year Labor Warranty / 15 Manufacturer Warranty .</li>
    <li>Customer to provide electronic Auto CAD for our use in creating submittal drawings ( As Built Drawings).</li>
    <li>Permits or associated fees are not included.</li>
    <li>Customer to provide a secured staging &amp; storage area for project related materials.</li>
    <li>All work proposed herein, shall be performed during normal business hours Monday- Friday.</li>
  </ul>
  <footer class="foot"><div class="stripe"><i></i><i></i><i></i></div><span class="url">www.nexbuildgroup.com</span><span class="num">3</span></footer>
</section>

<!-- Pricing -->
<section class="page p5">
  <header class="hdr"><div class="brand"><span class="mark"></span><span>NEXBUILD<small>TECHNOLOGIES</small></span></div><div class="sub">A Subsidiary of Guardline Alarm Division</div></header>
  <h2 class="band">PRICING</h2>
  <div class="price-table">
    <div class="col" style="left:10px"></div>
    <div class="col" style="left:155px"></div>
    <div class="th"><span style="left:2px">Sr.</span><span style="left:18px">MATERIALS &amp; LABOR</span><span style="left:163px">PRICE</span></div>
    <div class="tf">TOTAL PROJECT COST</div>
  </div>
  <footer class="foot"><div class="stripe"><i></i><i></i><i></i></div><span class="url">www.nexbuildgroup.com</span><span class="num">4</span></footer>
</section>

<!-- Payment -->
<section class="page p6">
  <header class="hdr"><div class="brand"><span class="mark"></span><span>NEXBUILD<small>TECHNOLOGIES</small></span></div><div class="sub">A Subsidiary of Guardline Alarm Division</div></header>
  <h2 class="band">PAYMENT SCHEDULE</h2>
  <ul class="bullets" style="top:70px">
    <li>Fifteen Percent(15%) of the proposed sell price shall be payable to NexBuild Technologies for project mobilization.</li>
    <li>Balance (85%) due upon completion of the Project.</li>
  </ul>
  <p class="pay-note">We appreciate your interest in NexBuild Technologies and we look forward to working together to bring your network infrastructure up to the best industry standards. The prices in this proposal are good for 90 days.</p>
  <h3 class="signed">SIGNED &amp; DATED</h3>
  <div class="sig-line" style="left:47px;top:189px;width:75px"></div>
  <div class="sig-line" style="left:184px;top:189px;width:50px"></div>
  <div class="sig" style="left:47px;top:190px">Customer Authorized Signature</div>
  <div class="sig" style="left:184px;top:190px">Date</div>
  <div class="sig" style="left:47px;top:218px">Leo Marquez</div>
  <div class="sig-line" style="left:47px;top:251px;width:75px"></div>
  <div class="sig-line" style="left:184px;top:251px;width:50px"></div>
  <div class="sig" style="left:47px;top:252px">NexBuild Technologies, Inc<br>Leo Marquez</div>
  <div class="sig" style="left:184px;top:252px">Date</div>
  <footer class="foot"><div class="stripe"><i></i><i></i><i></i></div><span class="url">www.nexbuildgroup.com</span><span class="num">5</span></footer>
</section>

<!-- References -->
<section class="page p7">
  <header class="hdr"><div class="brand"><span class="mark"></span><span>NEXBUILD<small>TECHNOLOGIES</small></span></div><div class="sub">A Subsidiary of Guardline Alarm Division</div></header>
  <h2 class="band tall">REFERENCES OF RECENT<br>LOW VOLTAGE PROJECTS</h2>
  <div class="ref-table">
    <div class="divider"></div>
    <div class="th"><span style="left:2px">S. No.</span><span style="left:23px">DETAILS</span></div>
    <span class="ref-no" style="top:14px">1</span>
    <div class="ref" style="top:12px"><b>Coastline Telephone Company</b><br>Ryan Cole<br>Director, Business Coordinator<br>(555)201-4410<br>(555)201-4488<br>ryan@coastlinetel.example</div>
    <span class="ref-no" style="top:54px">2</span>
    <div class="ref" style="top:52px"><b>Harborview Community School</b><br>1200 Harbor Lane, Bayview, FL 33000<br>Evan Ross<br>IT Director(555) 310-2291<br>(555) 310-2204<br>eross@harborview.example</div>
    <span class="ref-no" style="top:94px">3</span>
    <div class="ref" style="top:92px"><b>Sunrise Blooms</b><br>870 Orchard Way #210, Lakeside, FL 33001<br>Marco Diaz<br>IT Director<br>(555) 418-7730<br>(555) 418-7700 Ext: 120<br>mdiaz@sunriseblooms.example</div>
    <span class="ref-no" style="top:146px">4</span>
    <div class="ref" style="top:144px"><b>Clearpath Technology</b><br>45 Market Square, Suite 300, Westfield, FL 33002<br>Paul Weston<br>Director of Information Technology<br>(555) 522-6610<br>(555) 522-6699<br>pweston@clearpathtech.example</div>
  </div>
  <div class="clients">
    <span>Lumen Hotels</span><span>Bean House</span><span>Voxline</span><span>Shore City</span><span>Palmgate</span>
    <span>Signal Wireless</span><span>Crestway Inns</span><span>Northgate</span><span>Greenleaf</span><span></span>
  </div>
  <footer class="foot"><div class="stripe"><i></i><i></i><i></i></div><span class="url">www.nexbuildgroup.com</span><span class="num">6</span></footer>
</section>

<!-- Projects -->
<section class="page p8">
  <header class="hdr"><div class="brand"><span class="mark"></span><span>NEXBUILD<small>TECHNOLOGIES</small></span></div><div class="sub">A Subsidiary of Guardline Alarm Division</div></header>
  <h2 class="band">OUR RECENT PROJECTS</h2>
  <div class="proj-table">
    <div class="th">NAME</div>
    <div class="proj-row"><div class="pname">State Transit Agency Building</div><div class="shots" role="img" aria-label="Photos of cabling work and server racks at the transit agency building"><span></span><span></span><span></span></div></div>
    <div class="proj-row"><div class="pname">Bayside County Health Office</div><div class="shots" role="img" aria-label="Photos of network racks and a technician at the health office"><span></span><span></span><span></span></div></div>
    <div class="proj-row"><div class="pname">Vertex Data Center</div><div class="shots" role="img" aria-label="Photos of data center cabinets and cabling"><span></span><span></span><span></span></div></div>
    <div class="proj-row"><div class="pname">Arcline Miami</div><div class="shots" role="img" aria-label="Photos of an open office with installed workstations"><span></span><span></span><span></span></div></div>
    <div class="proj-row"><div class="pname">Signal Wireless Flagship Store</div><div class="shots" role="img" aria-label="Photos of a retail store interior and equipment room"><span></span><span></span><span></span></div></div>
    <div class="proj-row"><div class="pname">Clearskin Dermatology</div><div class="shots" role="img" aria-label="Photos of patch panels and network racks at the clinic"><span></span><span></span><span></span></div></div>
  </div>
  <footer class="foot"><div class="stripe"><i></i><i></i><i></i></div><span class="url">www.nexbuildgroup.com</span><span class="num">7</span></footer>
</section>

<!-- Certification -->
<section class="page p9">
  <header class="hdr"><div class="brand"><span class="mark"></span><span>NEXBUILD<small>TECHNOLOGIES</small></span></div><div class="sub">A Subsidiary of Guardline Alarm Division</div></header>
  <h2 class="band">CERTIFICATION</h2>
  <p class="cert-text">NBT will certify the wiring to ensure/guarantee the performance and quality of cabling installation . Results will provided to the customer at the completion of the installation.Copper Cable Certification Testing–The higher end CertiPro X100 is the most sophisticated RF measurement engine in any handheld tester. Able to support up to 3GHz frequency range, and testing all mode combination parameters (including TCL), it exceeds the level 2G accuracy specifications for copper certification testing.</p>
  <div class="cert-photo" role="img" aria-label="Photo of two handheld cable certification testers side by side"></div>
  <footer class="foot"><div class="stripe"><i></i><i></i><i></i></div><span class="url">www.nexbuildgroup.com</span><span class="num">8</span></footer>
</section>

</body>
</html>
```